Looking for updated Letterhead and Compliments Slips to go with our new updated logo. This stationary will be used for letters to suppliers and customers so needs to be practical while also quite classic.

We are an engineering company so needs to be clean and precise

Target Market(s)

SME'S and large automotive customers

Industry/Entity Type

Automotive

Font styles to use
Sans Serif

Colors
85acd3
0356a4
0792cd
33a6d7
85abd2
ffffff

Requirements
Must have
• Address details as below
• KT Fabrications Limited
• Marbury Close
• Rugby
• Warwickshire
• DN47 3XP, UK
• Telephone: +44 (0)1632 960418
• Fax: +44 (0)1632 960735
• Email: sales@ktfabrications.example
• Web: www.ktfabrications.example
Nice to have
• Nice to have some element of being a British Manufacturer

```html
<!DOCTYPE html>
<html lang="en">
<head>
<meta charset="utf-8">
<title>KT Fabrications – Letterhead and Compliments Slip</title>
<link rel="stylesheet" href="https://fonts.googleapis.com/css2?family=Source+Sans+3:wght@400;600&family=Pinyon+Script&display=swap">
<style>
  :root {
    --backdrop: #a9a8a9;
    --paper: #f5f4f2;
    --brand-blue: #0356a4;
    --brand-light: #85acd3;
    --text: #4a4a4a;
    --text-dark: #2b2b2b;
  }
  * { box-sizing: border-box; margin: 0; padding: 0; }
  html, body { width: 1200px; height: 770px; overflow: hidden; }
  body {
    background: var(--backdrop);
    font-family: "Source Sans 3", Arial, sans-serif;
    color: var(--text);
    position: relative;
  }
  .sheet { position: absolute; background: var(--paper); }

  /* Letterhead */
  .letterhead { left: 62px; top: 33px; width: 496px; height: 701px; }
  .brand {
    position: absolute; display: flex; flex-direction: column; align-items: center;
    color: var(--brand-blue); font-weight: 600; letter-spacing: 3px;
  }
  .brand-mark {
    width: 30px; height: 30px; border-radius: 50%; background: var(--brand-light);
  }
  .letterhead .brand { left: 0; right: 0; top: 34px; font-size: 14px; gap: 12px; }

  .letter-content { position: absolute; left: 35px; top: 197px; width: 425px; }
  .salutation { font-size: 13px; line-height: 16px; margin-bottom: 23px; color: var(--text); }
  .letter-body p {
    font-size: 8px; line-height: 12px; text-align: justify; hyphens: auto;
    margin-bottom: 12px;
  }
  .letter-body p:last-child { margin-bottom: 0; }
  .sign-off { margin-top: 25px; font-size: 8px; line-height: 10px; }
  .signature {
    margin: 6px 0 0 13px; width: 66px; height: 28px;
    background: linear-gradient(90deg, rgba(40,40,40,0.08), rgba(40,40,40,0.15), rgba(40,40,40,0.05));
    border-radius: 2px;
  }
  .signatory { margin: 8px 0 0 17px; font-size: 9px; line-height: 13px; }

  .letter-footer {
    position: absolute; left: 0; right: 0; top: 660px; text-align: center;
    font-size: 8px; line-height: 12px; color: var(--text-dark);
  }
  .letter-footer .label { color: var(--brand-blue); font-weight: 600; }

  /* Compliments slip */
  .compliments-slip { left: 583px; top: 477px; width: 561px; height: 254px; }
  .compliments-slip .brand { left: 25px; top: 20px; width: 132px; font-size: 10.5px; gap: 10px; letter-spacing: 2px; }
  .slip-address {
    position: absolute; right: 135px; top: 32px; text-align: right; font-style: normal;
    font-size: 8px; line-height: 10.5px; color: var(--text-dark);
  }
  .slip-divider { position: absolute; left: 431px; top: 25px; width: 1px; height: 45px; background: #9a9a9a; }
  .slip-contacts { position: absolute; left: 442px; top: 24px; list-style: none; }
  .slip-contacts li {
    display: flex; align-items: center; gap: 5px; height: 12px;
    font-size: 8px; color: var(--text-dark);
  }
  .slip-contacts svg { width: 8px; height: 8px; fill: var(--brand-blue); }
  .compliments-title {
    position: absolute; left: 103px; top: 142px;
    font-family: "Pinyon Script", cursive; font-size: 48px; color: var(--brand-blue);
  }
</style>
</head>
<body>

<section class="sheet letterhead">
  <div class="brand"><span class="brand-mark"></span><span>KT FABRICATIONS</span></div>

  <div class="letter-content">
    <p class="salutation">Dear Mr. Dawson,</p>

    <div class="letter-body">
      <p>Lorem ipsum dolor sit amet, consectetur adipiscing elit. Donec orci purus, luctus vitae dignissim eu, iaculis sed purus. Vivamus faucibus, ipsum nec aliquet viverra, leo mauris condimentum ligula, sit amet sagittis enim ligula quis arcu. Nam egestas tortor id nisi porttitor mattis. In tortor ante, ultricies in suscipit a, tempus non massa. Vivamus et auctor mi. Fusce vel massa nulla. Phasellus nec eros mauris, et scelerisque orci.</p>
      <p>Donec malesuada orci vitae nulla accumsan porta a id massa. Quisque accumsan iaculis magna sit amet fringilla. Maecenas consequat, magna eget tincidunt semper, odio nibh rutrum mi, id feugiat ante nisi eu risus. Vestibulum nunc orci, rhoncus a placerat in, ultricies in mi. Cras mattis varius eros, vel fringilla nisi suscipit eget. Quisque scelerisque sagittis nulla at porttitor.</p>
      <p>Sed id augue vitae urna euismod commodo aliquet a quam. Pellentesque arcu velit, cursus et malesuada ut, consequat et diam. Nullam erat sem, rhoncus id ullamcorper vitae, rhoncus et arcu. In ultricies ultricies nulla, ut rutrum nisi iaculis at. Donec eu magna a metus ornare faucibus. Fusce aliquet faucibus ultricies. Morbi semper, est id tincidunt gravida, sem arcu adipiscing lacus, ac bibendum nulla leo eu purus. Quisque nec diam sed risus consectetur accumsan quis quis nibh. Vestibulum id purus lorem.</p>
      <p>It is a long established fact that a reader will be distracted by the readable content of a page when looking at its layout. The point of using Lorem Ipsum is that it has a more-or-less normal distribution of letters, as opposed to using 'Content here, content here', making it look like readable English. Many desktop publishing packages</p>
    </div>

    <p class="sign-off">Sincerely,</p>
    <div class="signature" role="img" aria-label="Handwritten signature"></div>
    <p class="signatory">Peter Dawson<br>CEO/ Founder</p>
  </div>

  <footer class="letter-footer">
    <p>KT Fabrications Limited, Marbury Close, Rugby, Warwickshire</p>
    <p><span class="label">P:</span> +44 (0)1632 960418 &nbsp;<span class="label">F:</span> +44 (0)1632 960735 &nbsp;<span class="label">E:</span> sales@ktfabrications.example &nbsp;<span class="label">W:</span> www.ktfabrications.example</p>
  </footer>
</section>

<section class="sheet compliments-slip">
  <div class="brand"><span class="brand-mark"></span><span>KT FABRICATIONS</span></div>

  <address class="slip-address">
    KT Fabrications Limited<br>Marbury Close<br>Rugby, Warwickshire
  </address>
  <div class="slip-divider"></div>
  <ul class="slip-contacts">
    <li><svg viewBox="0 0 10 10"><path d="M2 0.5 L3.8 2.8 L2.8 3.9 Q4 6.2 6.1 7.2 L7.2 6.2 L9.5 8 L8.3 9.5 Q3.5 9 0.5 1.7 Z"/></svg>+44 (0)1632 960418</li>
    <li><svg viewBox="0 0 10 10"><rect x="2.5" y="0.5" width="5" height="3"/><rect x="0.5" y="3.5" width="9" height="4.5" rx="0.8"/><rect x="2.5" y="7" width="5" height="2.5"/></svg>+44 (0)1632 960735</li>
    <li><svg viewBox="0 0 10 10"><path d="M0.5 2 H9.5 V8.5 H0.5 Z M0.5 2 L5 5.5 L9.5 2" stroke="#f5f4f2" stroke-width="0.7"/></svg>sales@ktfabrications.example</li>
    <li><svg viewBox="0 0 10 10"><circle cx="5" cy="5" r="4.5"/><path d="M5 0.5 V9.5 M0.5 5 H9.5" stroke="#f5f4f2" stroke-width="0.7"/></svg>www.ktfabrications.example</li>
  </ul>

  <p class="compliments-title">With Compliments</p>
</section>

</body>
</html>
```